Website for an electrical contractor :)

We are after a web site which can show pictures of our jobs and our capability in a professional, creative and easily understood way.

----- Bramwell Electrical ------

We really want a visually good looking website with three sections

Section one:
'Completed projects'
We have a few pictures of jobs which we've completed and would like to show off with a brief description. (see uploads)

Section two:
'Our capabilities'
Just a list of what services we offer

Section three:
We would like a 'contact us' section which people can send us a short msg and upload a file for plans to be able to send to us. We would need their name, phone number and email details. We would also need a short privacy policy saying 'we do not disclose information to third parties'.
We also want to display our contact number and postal address

Good luck :)

Target Market(s)

Adults 25 years+
Business owners
Builders
Real estate agents

Industry/Entity Type

Electrical

Colors

Designer to choose colors to be used in the design.

Requirements
Must have
• Visually appealing
Easy to understand
In the 'Completed projects' section, must have a list for each project we do i can upload pictures for it.

```html
<!DOCTYPE html>
<html lang="en">
<head>
<meta charset="utf-8">
<title>Bramwell Electrical</title>
<link href="https://fonts.googleapis.com/css2?family=Open+Sans:wght@400;600;700&family=Ubuntu:wght@400;500;700&display=swap" rel="stylesheet">
<style>
:root{
  --red:#e21f26;
  --dark:#1b1b1b;
  --ink:#333;
  --muted:#777;
  --light:#f2f2f2;
  --grey:#e3e3e3;
  --footer:#121212;
  --white:#fff;
}
*{margin:0;padding:0;box-sizing:border-box}
html,body{width:781px;height:1200px;overflow:hidden}
body{font-family:"Open Sans",sans-serif;color:var(--ink);background:var(--white);position:relative}
.abs{position:absolute}
.topbar{left:0;top:0;width:781px;height:14px;background:var(--dark);color:#999;font-size:6px;line-height:14px}
.topbar .contact{left:105px}
.topbar .contact span{margin-right:14px}
.topbar .social{right:105px;top:0;display:flex}
.topbar .social i{display:block;width:15px;height:14px;border-left:1px solid var(--red)}
.topbar .social i:last-child{border-right:1px solid var(--red)}
.topbar .social i b{display:block;width:5px;height:5px;margin:4.5px auto;border-radius:50%;background:#888}
.topbar .social i:first-child b{background:var(--red)}
.header{left:0;top:14px;width:781px;height:48px;border-bottom:2px solid var(--red);background:var(--white)}
.brand{left:105px;top:13px;display:flex;align-items:center;gap:6px;font-family:"Ubuntu",sans-serif;font-size:24px;color:#444}
.brand .dot{width:10px;height:10px;border-radius:50%;background:var(--red)}
.nav{left:296px;top:16px;display:flex;align-items:center;font-size:7px;color:#333}
.nav a{color:inherit;text-decoration:none;margin-right:31px}
.nav .active{background:var(--red);color:#fff;font-weight:700;width:48px;height:17px;line-height:17px;text-align:center;margin-right:22px}
.hero{left:0;top:64px;width:781px;height:243px;background:linear-gradient(180deg,#5d8fc9 0%,#9ab8d6 28%,#b9b8b3 45%,#8f8a84 70%,#b5a48d 100%)}
.hero-tag{left:300px;top:166px;width:180px;height:78px;background:rgba(226,31,38,.88);color:#fff;font-family:"Ubuntu",sans-serif;font-weight:700;font-size:17.5px;line-height:22px;padding:17px 0 0 31px}
.dots{left:375px;top:293px;display:flex;gap:3px}
.dots i{width:8px;height:8px;border-radius:50%;background:var(--red)}
.dots i:nth-child(2){background:#fff}
.sec-title{width:781px;text-align:center;color:var(--red);font-family:"Ubuntu",sans-serif;font-weight:500;font-size:15px}
.sec-intro{left:200px;width:381px;text-align:center;font-size:5.6px;line-height:7.5px;color:#666}
.card{top:390px;width:180px;height:146px;border:1px solid #ddd;background:#fff;box-shadow:0 6px 6px -4px rgba(0,0,0,.25)}
.card.featured{background:var(--dark);border-color:var(--red)}
.card .photo{left:0;top:0;width:97px;height:144px}
.card .body{left:106px;top:22px;width:68px}
.card h3{font-family:"Ubuntu",sans-serif;color:var(--red);font-size:8.5px;font-weight:500}
.card h4{font-size:6.5px;font-weight:400;color:#444;margin-top:1px}
.card p{font-size:5.4px;line-height:8.5px;color:#888;margin-top:16px}
.card.featured h4{color:var(--red)}
.card.featured p{color:#fff}
.btn{display:block;width:49px;height:18px;line-height:18px;text-align:center;font-size:5.6px;font-weight:700;color:#fff;background:var(--dark);margin-top:10px}
.card.featured .btn,.btn.red{background:var(--red)}
.cap-band{left:0;top:561px;width:781px;height:380px;background:var(--light)}
.frame{top:639px;width:280px;height:176px;border:1px solid #d5d5d5;background:#fff;padding:5px}
.frame div{width:100%;height:100%}
.cap h2{font-family:"Ubuntu",sans-serif;font-weight:500;font-size:12px;color:#333}
.cap ul{list-style:none;display:grid;grid-template-columns:146px 130px;row-gap:5px;margin-top:8px}
.cap li{font-size:5.6px;font-weight:600;color:#444;height:10px;line-height:10px;padding-left:9px;position:relative}
.cap li:before{content:"";position:absolute;left:1px;top:4px;width:3px;height:3px;background:#333}
.cap li.hot{background:var(--red);color:#fff;width:132px}
.cap li.hot:before{background:#fff;left:5px}
.cap li.hot{padding-left:13px}
.cap .btn{width:58px;height:19px;line-height:19px;margin-top:11px;font-weight:600}
.contact-band{left:0;top:941px;width:781px;height:112px;background:var(--grey)}
.contact-band h2{left:105px;top:13px;font-family:"Ubuntu",sans-serif;font-weight:500;color:var(--red);font-size:13.5px}
.field{background:#fff;border:1px solid #e8e8e8;font-size:5.6px;color:#999;padding:4px 5px;height:15px}
.upload{left:544px;top:33px;width:132px;height:15px;background:#111;color:#fff;font-size:6.5px;font-weight:700;text-align:center;line-height:15px;border:1px solid var(--red)}
.submit{left:544px;top:56px;width:132px;height:34px;background:var(--red);color:#fff;font-size:8.5px;font-weight:700;text-align:center;line-height:34px}
.footer{left:0;top:1053px;width:781px;height:147px;background:var(--footer);color:#777;font-size:6px}
.footer h3{font-family:"Ubuntu",sans-serif;font-weight:400;color:var(--red);font-size:10px}
.f-brand{font-family:"Ubuntu",sans-serif;font-size:16px;color:#777;display:flex;align-items:center;gap:5px}
.f-brand i{width:8px;height:8px;border-radius:50%;background:var(--red)}
.f-social{display:flex;gap:6px;margin-top:14px}
.f-social i{width:14px;height:14px;border-radius:50%;background:#2a2a2a}
.f-social i:first-child{background:#2d5ab1}
.f-line{display:flex;gap:6px;align-items:flex-start;line-height:9px;margin-bottom:6px}
.f-line svg{flex:none;margin-top:1px}
.copy{left:0;top:1175px;width:781px;height:25px;border-top:1px solid var(--red);text-align:center;line-height:15px;font-size:5px;color:var(--red);background:var(--footer)}
</style>
</head>
<body>

<div class="abs topbar">
  <div class="abs contact"><span>&#9990; 04 1287 5530</span><span>&#9993; info@bramwellelectrical.com.au</span></div>
  <div class="abs social"><i><b></b></i><i><b></b></i><i><b></b></i><i><b></b></i></div>
</div>

<header class="abs header">
  <div class="abs brand"><span class="dot"></span>Bramwell</div>
  <nav class="abs nav">
    <a class="active" href="#">Home</a>
    <a href="#">About Us</a>
    <a href="#">Our Projects</a>
    <a href="#">Our Capabilities</a>
    <a href="#" style="margin-right:35px">Blog</a>
    <a href="#">Contact Us</a>
  </nav>
</header>

<section class="abs hero" role="img" aria-label="Photo of a new concrete commercial building under construction with a service van parked out front"></section>
<div class="abs hero-tag">Development<br>&amp; Installation</div>
<div class="abs dots"><i></i><i></i><i></i></div>

<h2 class="abs sec-title" style="top:333px">Our Projects</h2>
<p class="abs sec-intro" style="top:359px">Lorem Ipsum is simply dummy text of the printing and typesetting industry. Lorem Ipsum has been the industry's standard dummy text ever since the 1500s, when an unknown printer took a galley of type and scrambled it to make a type specimen book.</p>

<article class="abs card featured" style="left:105px">
  <div class="abs photo" role="img" aria-label="Photo of a finished lounge room with white sofas" style="background:linear-gradient(180deg,#d9d6d0,#b7b0a6 70%,#6a625b)"></div>
  <div class="abs body"><h3>Lorem Ipsum</h3><h4>is simply dummy</h4><p>Lorem Ipsum is simply dummy text of the printing.</p><a class="btn">Read More</a></div>
</article>
<article class="abs card" style="left:300px">
  <div class="abs photo" role="img" aria-label="Photo of conduit laid over slab reinforcement on a building site" style="background:linear-gradient(180deg,#9fb4c9,#8c8074 40%,#5b544d)"></div>
  <div class="abs body"><h3>Lorem Ipsum</h3><h4>is simply dummy</h4><p>Lorem Ipsum is simply dummy text of the printing.</p><a class="btn">Read More</a></div>
</article>
<article class="abs card" style="left:496px">
  <div class="abs photo" role="img" aria-label="Photo of a new kitchen with downlights and stone benchtops" style="background:linear-gradient(180deg,#cfc9c0,#a59b8f 60%,#4e4944)"></div>
  <div class="abs body"><h3>Lorem Ipsum</h3><h4>is simply dummy</h4><p>Lorem Ipsum is simply dummy text of the printing.</p><a class="btn">Read More</a></div>
</article>

<div class="abs cap-band"></div>
<h2 class="abs sec-title" style="top:582px">Our Capabilities</h2>
<p class="abs sec-intro" style="top:609px">Lorem Ipsum is simply dummy text of the printing and typesetting industry. Lorem Ipsum has been the industry's standard dummy text ever since the 1500s, when an unknown printer took a galley of type and scrambled it to make a type specimen book.</p>

<div class="abs frame" style="left:104px"><div role="img" aria-label="Photo of new residential townhouses with a paved driveway" style="background:linear-gradient(180deg,#3f8de0 0%,#8cbce8 35%,#8d8578 60%,#5f5c58 100%)"></div></div>
<div class="abs frame" style="left:398px"><div role="img" aria-label="Photo of a concrete commercial warehouse under a blue sky" style="background:linear-gradient(180deg,#1d4fb0 0%,#5a86c9 30%,#c3c2bd 55%,#a8a6a1 100%)"></div></div>

<div class="abs cap" style="left:104px;top:827px">
  <h2>Residential Capability Statement</h2>
  <ul>
    <li class="hot">24hr Support / faults</li><li>Ceiling fans</li>
    <li>Mains/sub mains cabling</li><li>Exhaust fans</li>
    <li>RCD (Safety Switch) installations</li><li>Kitchen / Bathroom Projects</li>
  </ul>
  <a class="btn red">Read More</a>
</div>
<div class="abs cap" style="left:397px;top:827px">
  <h2>Commercial / Industrial Capability Statement</h2>
  <ul>
    <li>24hr Support / faults</li><li>Phone/data points</li>
    <li>Lighting/power design and consultation</li><li>Data cabinets</li>
    <li>Emergency and exit lighting</li><li>Data Networking</li>
  </ul>
  <a class="btn red">Read More</a>
</div>

<section class="abs contact-band">
  <h2 class="abs">Contact From</h2>
  <div class="abs field" style="left:105px;top:33px;width:132px">Enter Your Name :</div>
  <div class="abs field" style="left:252px;top:33px;width:131px">Enter Your Email :</div>
  <div class="abs field" style="left:398px;top:33px;width:132px">Enter Your Phone :</div>
  <div class="abs field" style="left:105px;top:56px;width:425px;height:34px">Massage :</div>
  <div class="abs upload">Upload File</div>
  <div class="abs submit">SUBMIT</div>
</section>

<footer class="abs footer">
  <div class="abs" style="left:105px;top:26px;width:135px">
    <div class="f-brand"><i></i>Bramwell</div>
    <p style="margin-top:16px;line-height:8.5px;font-size:5.4px">Lorem Ipsum is simply dummy text of the printing and typesetting industry. Lorem Ipsum has been the industry's standard dummy text ever since</p>
  </div>
  <div class="abs" style="left:251px;top:23px">
    <h3>Follow Us On</h3>
    <div class="f-social"><i></i><i></i><i></i></div>
  </div>
  <div class="abs" style="left:397px;top:23px;width:135px">
    <h3>Location</h3>
    <div class="f-line" style="margin-top:10px"><svg width="5" height="7" viewBox="0 0 10 14"><path d="M5 0a5 5 0 0 0-5 5c0 4 5 9 5 9s5-5 5-9a5 5 0 0 0-5-5zm0 7a2 2 0 1 1 0-4 2 2 0 0 1 0 4z" fill="#777"/></svg><span>P.O Box 517 Harbourside W.A<br>6019 A.B.N: 48 210 993 057</span></div>
  </div>
  <div class="abs" style="left:544px;top:23px">
    <h3>Contact Info</h3>
    <div style="margin-top:10px">
      <div class="f-line"><svg width="6" height="6" viewBox="0 0 10 10"><path d="M2 0l2 2-1 2 3 3 2-1 2 2-2 2C4 10 0 6 0 2z" fill="#777"/></svg>04 1287 5530</div>
      <div class="f-line"><svg width="6" height="6" viewBox="0 0 10 10"><rect x="2" y="0" width="6" height="3" fill="#777"/><rect x="0" y="3" width="10" height="5" fill="#777"/><rect x="2" y="6" width="6" height="4" fill="#999"/></svg>08 9312 4408</div>
      <div class="f-line"><svg width="7" height="5" viewBox="0 0 14 10"><rect width="14" height="10" fill="#777"/><path d="M0 0l7 6 7-6" stroke="#121212" fill="none"/></svg>info@bramwellelectrical.com.au</div>
    </div>
  </div>
</footer>
<div class="abs copy">All Copyrigts Reserved © Bramwell Electrical 2015. Privacy Policy</div>

</body>
</html>
```